Outdoor Company Business Card design

We are an outdoor adventure company needing a business card. We sell outdoor adventures and clothing. Please use our logo in the business card. We are looking for something unique but delivers a clear message as to who we are. Please be creative

Target Market(s)

Outdoor adventures

Industry/Entity Type

Business

Contact Information for Business Card

Business name: TrailBrook If using the logo, no need to have a spot for the name
Owner / CEO: Owen Pardle
Website: TrailBrook.example
Facebook: Social.example/TrailBrook
Instagram: @pardle_owen
phone number: 555-384-7120
Email: Pardleteams@TrailBrook.example

Colors

Designer to choose colors to be used in the design.

Requirements
Must have
• The business card must include the details mentioned above. ie logo, my name, email, facebook, instagram, website, and phone number.
Should not have
• should not be cluttered or look messy

```html
<!DOCTYPE html>
<html lang="en">
<head>
<meta charset="utf-8">
<title>TrailBrook Business Card</title>
<link href="https://fonts.googleapis.com/css2?family=Josefin+Sans:wght@300;400;600;700&display=swap" rel="stylesheet">
<style>
  :root {
    --brand-blue: #1077bd;
    --brand-orange: #f15a29;
    --paper: #ffffff;
    --page: #ffffff;
    --text-light: #ffffff;
  }
  html, body {
    margin: 0;
    padding: 0;
    width: 1200px;
    height: 1000px;
    overflow: hidden;
    background: var(--page);
  }
  .canvas {
    position: relative;
    width: 1200px;
    height: 1000px;
    font-family: "Josefin Sans", "Futura", sans-serif;
  }
  .card {
    position: absolute;
    left: 282px;
    top: 274px;
    width: 739px;
    height: 382px;
    background: var(--paper);
    box-shadow: 0 0 8px rgba(0,0,0,0.45);
  }
  .brand-side {
    position: absolute;
    left: 0;
    top: 0;
    width: 378px;
    height: 382px;
    display: flex;
    align-items: center;
    justify-content: center;
  }
  .wordmark {
    display: flex;
    align-items: center;
    gap: 12px;
    margin-top: 24px;
  }
  .wordmark-dot {
    width: 20px;
    height: 20px;
    background: var(--brand-orange);
  }
  .wordmark-name {
    font-weight: 700;
    font-size: 39px;
    letter-spacing: 1px;
    color: var(--brand-blue);
    text-transform: uppercase;
    line-height: 1;
    padding-top: 6px;
  }
  .contact-side {
    position: absolute;
    left: 393px;
    top: 0;
    width: 346px;
    height: 382px;
    background: var(--brand-blue);
  }
  .icon-rail {
    position: absolute;
    left: 378px;
    top: 65px;
    width: 28px;
    height: 252px;
    background: var(--brand-orange);
  }
  .icon {
    position: absolute;
    left: 3px;
    width: 22px;
    height: 22px;
  }
  .owner-name {
    position: absolute;
    left: 406px;
    width: 333px;
    top: 76px;
    margin: 0;
    text-align: center;
    font-weight: 400;
    font-size: 30px;
    font-variant: small-caps;
    letter-spacing: 3px;
    line-height: 1;
    color: var(--text-light);
  }
  .contact-line {
    position: absolute;
    left: 406px;
    width: 333px;
    margin: 0;
    text-align: center;
    font-weight: 300;
    font-size: 14px;
    letter-spacing: 2px;
    line-height: 1;
    color: var(--text-light);
  }
  .contact-line.email {
    font-size: 13px;
    letter-spacing: 1.5px;
  }
</style>
</head>
<body>
<div class="canvas">
  <div class="card">
    <div class="brand-side">
      <div class="wordmark">
        <span class="wordmark-dot"></span>
        <span class="wordmark-name">TrailBrook</span>
      </div>
    </div>

    <div class="contact-side"></div>

    <div class="icon-rail">
      <svg class="icon" style="top:15px" viewBox="0 0 22 22">
        <circle cx="11" cy="7" r="4.5" fill="#fff"/>
        <path d="M3 21 C3 14 19 14 19 21 Z" fill="#fff"/>
      </svg>
      <svg class="icon" style="top:61px" viewBox="0 0 22 22" fill="none" stroke="#fff" stroke-width="1.2">
        <circle cx="11" cy="11" r="8"/>
        <ellipse cx="11" cy="11" rx="3.5" ry="8"/>
        <line x1="3" y1="11" x2="19" y2="11"/>
        <line x1="4.5" y1="7" x2="17.5" y2="7"/>
        <line x1="4.5" y1="15" x2="17.5" y2="15"/>
      </svg>
      <svg class="icon" style="top:104px" viewBox="0 0 22 22">
        <rect x="1" y="1" width="20" height="20" rx="2" fill="#fff"/>
      </svg>
      <svg class="icon" style="top:149px" viewBox="0 0 22 22">
        <circle cx="11" cy="11" r="9.5" fill="#fff"/>
      </svg>
      <svg class="icon" style="top:192px" viewBox="0 0 22 22">
        <path d="M2 8 C2 4 20 4 20 8 L20 10 L15 10 L15 8 L7 8 L7 10 L2 10 Z" fill="#fff"/>
        <path d="M5 11 L17 11 L19 18 L3 18 Z" fill="#fff"/>
        <circle cx="11" cy="14.5" r="2" fill="#f15a29"/>
      </svg>
      <svg class="icon" style="top:228px" viewBox="0 0 22 22">
        <rect x="1" y="5" width="20" height="13" fill="#fff"/>
        <path d="M1.5 5.5 L11 12.5 L20.5 5.5" fill="none" stroke="#f15a29" stroke-width="1"/>
      </svg>
    </div>

    <h1 class="owner-name">Owen Pardle</h1>
    <p class="contact-line" style="top:132px">TrailBrook.example</p>
    <p class="contact-line" style="top:174px">Social.example/TrailBrook</p>
    <p class="contact-line" style="top:219px">@pardle_owen</p>
    <p class="contact-line" style="top:261px">555-384-7120</p>
    <p class="contact-line email" style="top:297px">Pardleteams@TrailBrook.example</p>
  </div>
</div>
</body>
</html>
```